BRENLO CAPITAL INSTITUTIONAL PRESENTATION

To create a powerpoint presentation with selected art and text.
Target Market(s)
Potential Investors for the fund
Industry/Entity Type
Finance
Font styles to use
Sans Serif
Colors
0692cd
0255a3
Requirements
Must have
- Unique art, to look sober and professional
Nice to have
- Modern look
Should not have
- Red as color...

```html
<!DOCTYPE html>
<html lang="en">
<head>
<meta charset="utf-8">
<title>Brenlo Capital – Institutional Presentation</title>
<link href="https://fonts.googleapis.com/css2?family=Raleway:wght@300;400;500;600&display=swap" rel="stylesheet">
<style>
:root{
  --blue:#0692cd;
  --blue-deep:#1a7fcf;
  --navy:#0255a3;
  --slate:#46535a;
  --ink:#2a2f33;
  --grey:#6b7378;
  --line:#c9d6e0;
  --rule:#5a9be0;
  --disc:#e4f1fa;
  --page:#ffffff;
}
*{box-sizing:border-box;margin:0;padding:0}
html,body{width:818px;height:1200px;overflow:hidden;background:var(--page)}
body{position:relative;font-family:"Raleway",Arial,sans-serif;color:var(--ink)}
.slide{position:absolute;width:371px;height:209px;background:#fff;box-shadow:1px 2px 4px rgba(0,0,0,.35);overflow:hidden}
.abs{position:absolute}
.center{text-align:center}
.brand{font-weight:500;letter-spacing:.5px;white-space:nowrap}
.square{display:inline-block;vertical-align:middle;background:var(--blue)}
.disc{position:absolute;border-radius:50%;background:var(--disc)}
.corner-dot{position:absolute;left:343px;top:11px;width:12px;height:12px;border-radius:50%;background:var(--blue)}
.tiny{font-size:4.2px;line-height:6px;color:var(--grey)}
.footer-rule{position:absolute;left:0;right:0;top:196px;height:2px;background:var(--rule)}
.footer{position:absolute;left:0;right:0;top:200px;font-size:3.6px;color:var(--grey)}
.footer .date{position:absolute;left:17px}
.footer .mark{position:absolute;left:0;right:0;text-align:center;font-size:6px;color:var(--ink);top:-1px}
.footer .num{position:absolute;right:17px}
.heading{position:absolute;left:0;right:0;top:17px;text-align:center;font-weight:300;font-size:12px;letter-spacing:.6px;color:var(--slate)}
.photo{position:absolute}
.box-title{font-weight:300;font-size:11px;color:#fff;text-align:center;letter-spacing:.5px}
.box-text{font-size:4.6px;line-height:7px;color:#fff;text-align:center}
.agenda-item{position:absolute;left:189px;width:145px;height:22px;border-top:1px solid var(--line)}
.agenda-item .n{position:absolute;left:1px;top:7px;font-size:10px;color:var(--blue-deep)}
.agenda-item .t{position:absolute;left:17px;top:12px;font-size:4.4px;color:var(--ink)}
.cell{position:absolute;width:111px;height:46px}
.cell.text{background:var(--blue-deep);color:#fff;text-align:center;padding:4px 6px}
.cell.text h4{font-weight:400;font-size:4.8px;margin-bottom:2px}
.cell.text p{font-size:3.6px;line-height:4.6px}
.chart{position:absolute;display:flex;align-items:flex-end;justify-content:space-between}
.chart .bar{position:relative;width:6px;height:100%}
.chart .fill{position:absolute;left:0;right:0;bottom:0;background:var(--blue-deep)}
.chart.track .bar{background:#dde2e5}
</style>
</head>
<body>

<!-- Cover A -->
<section class="slide" style="left:27px;top:14px">
  <div class="abs" style="left:38px;top:22px;width:296px;height:160px;border:1px solid #bfe0f2"></div>
  <div class="abs" style="left:18px;top:34px;width:336px;height:98px;background:var(--slate)"></div>
  <div class="abs center" style="left:18px;top:74px;width:336px">
    <span class="square" style="width:9px;height:9px;margin-right:5px"></span><span class="brand" style="font-size:10px;color:#fff;vertical-align:middle">BRENLO CAPITAL</span>
  </div>
  <div class="abs center" style="left:0;right:0;top:166px;font-size:12.5px;color:var(--blue-deep);letter-spacing:.6px">BRENLO Macro Global Fund</div>
  <div class="abs center" style="left:0;right:0;top:185px;font-size:3.6px;color:var(--ink)">LOREM IPSUM DOLOR | 01.01.2018</div>
</section>

<!-- Cover B -->
<section class="slide" style="left:415px;top:14px">
  <div class="abs" style="left:38px;top:22px;width:296px;height:160px;border:1px solid #b8bcbf"></div>
  <div class="abs" style="left:18px;top:38px;width:336px;height:58px;background:var(--blue-deep)"></div>
  <div class="abs center" style="left:18px;top:54px;width:336px;font-size:12px;color:#17324a;letter-spacing:.6px">BRENLO Macro Global Fund</div>
  <div class="abs center" style="left:131px;top:74px;width:110px;height:10px;border:1px solid #fff;font-size:3.6px;line-height:8px;color:#fff">LOREM IPSUM DOLOR | 01.01.2018</div>
  <div class="abs center" style="left:0;right:0;top:186px;background:#fff;padding-top:2px">
    <span class="square" style="width:8px;height:8px;margin-right:4px"></span><span class="brand" style="font-size:9.5px;color:var(--ink);vertical-align:middle">BRENLO CAPITAL</span>
  </div>
</section>

<!-- Cover C -->
<section class="slide" style="left:27px;top:236px">
  <div class="photo" role="img" aria-label="Aerial photograph of a city skyline with office towers" style="left:16px;top:15px;width:339px;height:98px;border:1px solid var(--rule);background:linear-gradient(180deg,#e6ebef 0%,#b9c3ca 40%,#8c979f 75%,#a7b1b8 100%)"></div>
  <div class="abs center" style="left:0;right:0;top:130px">
    <span class="square" style="width:14px;height:14px;margin-right:6px"></span><span class="brand" style="font-size:18px;color:var(--ink);vertical-align:middle">BRENLO CAPITAL</span>
  </div>
  <div class="abs center" style="left:0;right:0;top:184px;font-size:5.5px;letter-spacing:.8px;color:var(--ink)">BRENLO Macro Global Fund</div>
  <div class="abs center" style="left:0;right:0;top:193px;font-size:3.6px;color:var(--blue-deep)">LOREM IPSUM DOLOR | 01.01.2018</div>
</section>

<!-- Introduction -->
<section class="slide" style="left:415px;top:236px">
  <div class="photo" role="img" aria-label="Blurred blue office background photograph" style="left:17px;top:32px;width:337px;height:144px;background:linear-gradient(120deg,#2a8fd6 0%,#1b7cc8 45%,#3b95d4 75%,#1f7dc4 100%)"></div>
  <div class="abs center" style="left:17px;top:70px;width:170px;font-size:5px;letter-spacing:1px;color:#16324b">BRENLO CAPITAL</div>
  <div class="abs center" style="left:17px;top:80px;width:170px;font-size:14px;font-weight:300;color:#fff;letter-spacing:.5px">INTRODUCTION</div>
  <div class="abs" style="left:86px;top:120px;width:32px;height:32px;border-radius:50%;background:rgba(255,255,255,.18)"></div>
  <div class="abs" style="left:186px;top:44px;width:1px;height:118px;background:rgba(255,255,255,.45)"></div>
  <div class="abs center" style="left:196px;top:58px;width:146px;font-size:3.8px;line-height:5px;color:#fff">
    <p style="margin-bottom:4px">Founded in 2016, an independent asset management firm focused on generating superior returns.</p>
    <p style="margin-bottom:4px">Investment decisions use fundamental macroeconomic analysis, balancing long term results with short term positioning.</p>
    <p style="margin-bottom:4px">Expertise in FX, interest rates and equity strategies, both in Brazil and globally.</p>
    <p style="margin-bottom:4px">Among the largest inflows of any hedge fund in 2017, and again in 2018.</p>
    <p>*Source (see note)</p>
  </div>
  <div class="footer-rule"></div>
  <div class="footer"><span class="date">DATE | LOREM IPSUM</span><span class="mark brand">BRENLO CAPITAL</span><span class="num">3</span></div>
</section>

<!-- Agenda -->
<section class="slide" style="left:27px;top:457px">
  <div class="disc" style="left:56px;top:64px;width:80px;height:80px"></div>
  <div class="agenda-item" style="top:36px"><span class="n">01</span><span class="t">LOREM IPSUM DOLOR SIT AMET</span></div>
  <div class="agenda-item" style="top:58px"><span class="n">02</span><span class="t">LOREM IPSUM DOLOR SIT AMET</span></div>
  <div class="agenda-item" style="top:80px"><span class="n">03</span><span class="t">LOREM IPSUM DOLOR SIT AMET</span></div>
  <div class="agenda-item" style="top:102px"><span class="n">04</span><span class="t">LOREM IPSUM DOLOR SIT AMET</span></div>
  <div class="agenda-item" style="top:124px"><span class="n">05</span><span class="t">LOREM IPSUM DOLOR SIT AMET</span></div>
  <div class="agenda-item" style="top:146px;border-bottom:1px solid var(--line)"><span class="n">06</span><span class="t">LOREM IPSUM DOLOR SIT AMET</span></div>
  <div class="footer-rule"></div>
  <div class="footer"><span class="date">DATE | LOREM IPSUM</span><span class="mark brand">BRENLO CAPITAL</span><span class="num">4</span></div>
</section>

<!-- Section divider -->
<section class="slide" style="left:415px;top:457px">
  <div class="disc" style="left:255px;top:32px;width:80px;height:80px"></div>
  <div class="abs center" style="left:255px;top:57px;width:80px;font-size:22px;font-weight:300;color:var(--blue-deep)">01</div>
  <div class="abs" style="left:19px;top:140px;width:195px;text-align:right;font-size:11px;font-weight:300;letter-spacing:1px;color:var(--slate)">LOREM&nbsp; IPSUM</div>
  <div class="abs" style="left:19px;top:157px;width:214px;height:1px;background:var(--line)"></div>
  <div class="footer-rule"></div>
  <div class="footer"><span class="date">DATE | LOREM IPSUM</span><span class="mark brand">BRENLO CAPITAL</span><span class="num">5</span></div>
</section>

<!-- Executive summary -->
<section class="slide" style="left:27px;top:678px">
  <h2 class="heading">EXECUTIVE SUMMARY</h2>
  <div class="corner-dot"></div>
  <p class="abs center" style="left:30px;right:30px;top:36px;font-size:4.2px;line-height:5.4px;color:var(--ink)">Lorem ipsum dolor sit amet, consectetuer adipiscing elit. Aenean commodo ligula eget dolor. Aenean massa. Cum sociis natoque penatibus et magnis dis parturient montes, nascetur ridiculus mus, pellentesque.</p>
  <div class="cell photo" role="img" aria-label="Photograph of hands working at a laptop" style="left:17px;top:74px;background:linear-gradient(135deg,#eef2f5,#b8c6d2)"></div>
  <div class="cell text" style="left:130px;top:74px"><h4>LOREM IPSUM DOLOR SIT</h4><p>In enim justo, rhoncus ut, imperdiet a, venenatis vitae, justo. Nullam dictum felis eu pede mollis pretium. Integer tincidunt.</p></div>
  <div class="cell photo" role="img" aria-label="Photograph of a business meeting" style="left:243px;top:74px;background:linear-gradient(135deg,#dfe6ee,#8ea2b8)"></div>
  <div class="cell text" style="left:17px;top:122px"><h4>LOREM IPSUM DOLOR SIT</h4><p>In enim justo, rhoncus ut, imperdiet a, venenatis vitae, justo. Nullam dictum felis eu pede mollis pretium. Integer tincidunt.</p></div>
  <div class="cell photo" role="img" aria-label="Photograph of a pen over printed documents" style="left:130px;top:122px;background:linear-gradient(135deg,#f3f5f4,#c7cfd0)"></div>
  <div class="cell text" style="left:243px;top:122px"><h4>LOREM IPSUM DOLOR SIT</h4><p>In enim justo, rhoncus ut, imperdiet a, venenatis vitae, justo. Nullam dictum felis eu pede mollis pretium. Integer tincidunt.</p></div>
  <div class="footer-rule"></div>
  <div class="footer"><span class="date">DATE | LOREM IPSUM</span><span class="mark brand">BRENLO CAPITAL</span><span class="num">7</span></div>
</section>

<!-- The opportunity -->
<section class="slide" style="left:415px;top:678px">
  <h2 class="heading">THE OPPORTUNITY</h2>
  <div class="corner-dot"></div>
  <div class="abs" style="left:22px;top:56px;width:157px;height:113px;background:var(--blue-deep)">
    <div class="abs box-title" style="left:0;right:0;top:17px">BRAZIL</div>
    <div class="abs" style="left:30px;right:0;top:38px;height:1px;background:rgba(255,255,255,.7)"></div>
    <div class="abs box-text" style="left:6px;right:6px;top:55px">Most recent recession saw asset prices fall<br>Now well below global comparisons<br>Major opportunities in Fixed Income and FX</div>
  </div>
  <div class="abs" style="left:191px;top:56px;width:157px;height:113px;background:var(--slate)">
    <div class="abs box-title" style="left:0;right:0;top:17px;color:var(--blue)">OTHER EMS</div>
    <div class="abs" style="left:0;right:30px;top:38px;height:1px;background:rgba(255,255,255,.7)"></div>
    <div class="abs box-text" style="left:10px;right:10px;top:51px;line-height:5.6px">Evidence that Brazil provides a template for returns elsewhere<br><br>Valuations in EM trail those in DM<br><br>Mix of strategies is best way to generate performance; and protect portfolio from adverse short-term volatility</div>
  </div>
  <div class="footer-rule"></div>
  <div class="footer"><span class="date">DATE | LOREM IPSUM</span><span class="mark brand">BRENLO CAPITAL</span><span class="num">8</span></div>
</section>

<!-- Consistent returns -->
<section class="slide" style="left:27px;top:898px">
  <h2 class="heading">CONSISTENT RETURNS</h2>
  <div class="corner-dot"></div>
  <div class="abs" style="left:19px;top:57px;width:145px">
    <div style="font-size:5.5px;color:var(--blue-deep);margin-bottom:2px">LOREM IPSUM</div>
    <p class="tiny" style="font-size:3.4px;line-height:4.4px">In enim justo, rhoncus ut, imperdiet a, venenatis vitae, justo. Nullam dictum felis eu pede mollis pretium. Integer tincidunt. Cras dapibus vivamus elementum semper nisi aenean vulputate.</p>
    <p class="tiny" style="font-size:3.4px;line-height:4.4px;margin-top:3px">Aliquam lorem ante, dapibus in, viverra quis, feugiat a, tellus. Phasellus viverra nulla ut metus varius laoreet quisque rutrum.</p>
  </div>
  <div class="abs tiny" style="left:180px;top:55px;font-size:3px;line-height:8.4px;text-align:right;width:8px">0.8<br>0.6<br>0.4<br>0.2<br>0</div>
  <div class="chart track" style="left:191px;top:56px;width:166px;height:42px">
    <div class="bar"><div class="fill" style="height:62%"></div></div>
    <div class="bar"><div class="fill" style="height:48%"></div></div>
    <div class="bar"><div class="fill" style="height:36%"></div></div>
    <div class="bar"><div class="fill" style="height:26%"></div></div>
    <div class="bar"><div class="fill" style="height:30%"></div></div>
    <div class="bar"><div class="fill" style="height:34%"></div></div>
    <div class="bar"><div class="fill" style="height:38%"></div></div>
    <div class="bar"><div class="fill" style="height:32%"></div></div>
    <div class="bar"><div class="fill" style="height:34%"></div></div>
    <div class="bar"><div class="fill" style="height:44%"></div></div>
    <div class="bar"><div class="fill" style="height:54%"></div></div>
    <div class="bar"><div class="fill" style="height:50%"></div></div>
  </div>
  <div class="abs tiny" style="left:191px;top:99px;width:166px;font-size:3px;display:flex;justify-content:space-between"><span>Text</span><span>Text</span><span>Text</span><span>Text</span><span>Text</span><span>Text</span><span>Text</span><span>Text</span><span>Text</span><span>Text</span><span>Text</span><span>Text</span></div>
  <div class="abs" style="left:17px;top:116px;width:337px;height:1px;background:var(--line)"></div>
  <div class="abs tiny" style="left:14px;top:132px;font-size:3px;line-height:8px;text-align:right;width:10px">100%<br>80%<br>60%<br>40%<br>20%<br>0%</div>
  <div class="chart" style="left:28px;top:134px;width:168px;height:41px">
    <div class="bar"><div class="fill" style="height:88%"></div></div>
    <div class="bar"><div class="fill" style="height:84%"></div></div>
    <div class="bar"><div class="fill" style="height:80%"></div></div>
    <div class="bar"><div class="fill" style="height:74%"></div></div>
    <div class="bar"><div class="fill" style="height:70%"></div></div>
    <div class="bar"><div class="fill" style="height:82%"></div></div>
    <div class="bar"><div class="fill" style="height:70%"></div></div>
    <div class="bar"><div class="fill" style="height:74%"></div></div>
    <div class="bar"><div class="fill" style="height:78%"></div></div>
    <div class="bar"><div class="fill" style="height:82%"></div></div>
    <div class="bar"><div class="fill" style="height:86%"></div></div>
    <div class="bar"><div class="fill" style="height:80%"></div></div>
  </div>
  <div class="abs tiny" style="left:28px;top:176px;width:168px;font-size:3px;display:flex;justify-content:space-between"><span>Text</span><span>Text</span><span>Text</span><span>Text</span><span>Text</span><span>Text</span><span>Text</span><span>Text</span><span>Text</span><span>Text</span><span>Text</span><span>Text</span></div>
  <div class="abs" style="left:211px;top:133px;width:145px">
    <div style="font-size:5.5px;color:var(--blue-deep);margin-bottom:2px">LOREM IPSUM</div>
    <p class="tiny" style="font-size:3.4px;line-height:4.4px">In enim justo, rhoncus ut, imperdiet a, venenatis vitae, justo. Nullam dictum felis eu pede mollis pretium. Integer tincidunt. Cras dapibus vivamus elementum semper nisi.</p>
    <p class="tiny" style="font-size:3.4px;line-height:4.4px;margin-top:3px">Aliquam lorem ante, dapibus in, viverra quis, feugiat a, tellus. Phasellus viverra nulla ut metus varius laoreet.</p>
  </div>
  <div class="footer-rule"></div>
  <div class="footer"><span class="date">DATE | LOREM IPSUM</span><span class="mark brand">BRENLO CAPITAL</span><span class="num">9</span></div>
</section>

<!-- Contact -->
<section class="slide" style="left:415px;top:898px">
  <div class="photo" role="img" aria-label="Portrait photograph of a smiling businessman in a dark suit with arms crossed" style="left:16px;top:10px;width:132px;height:199px;background:linear-gradient(180deg,#f2f2f2 0%,#e2e2e2 40%,#3a3d42 62%,#22252a 100%)"></div>
  <div class="abs" style="left:156px;top:40px;white-space:nowrap">
    <span class="square" style="width:14px;height:14px;margin-right:6px"></span><span class="brand" style="font-size:18px;color:var(--ink);vertical-align:middle">BRENLO CAPITAL</span>
  </div>
  <div class="abs" style="left:266px;top:83px;font-size:4.8px;line-height:6.4px;color:var(--grey)">
    <div style="color:var(--blue-deep)">contato@brenlocapital.com</div>
    <div style="margin-top:6px">Tel. +55 21 3000-4100</div>
    <div style="margin-top:6px">Rua das Palmas 48<br>Sala 310 – Centro<br>Rio de Janeiro – RJ – Brasil – CEP<br>20000-100</div>
  </div>
</section>

</body>
</html>
```